Business Card Design

Stronger Living Compact for the Plains is a partnership of twenty different health organisations in the western suburbs of Melbourne, working together to improve the health of the local community. The western suburbs of Melbourne is one of the fastest growing and most culturally diverse populations in Australia and its communities have some of the poorest health outcomes in Australia.
Please see location for copy of the SLCP:
http://kvrt.com.au/fileadmin/filemount/pdf_files/SLCFTP_13_FINAL_JUNE_2012.pdf

Reason: Hello. I've extended the deadline because in the brief I made a confusing mention about a logo, but I actually meant the 'Stronger Living Compact for the Plains' jpg that I had already attached. Sorry about the confusion Thanks Fiona

Hello, Thanks for the designs I have already received. I have extended the deadline because I made a confusing reference to a logo in my brief, but I was talking about the 'Stronger Living Compact for the Plains' jpg I had already attached. There is no other logo for me to provide.

Thanks, Fiona

Target Market(s)

Health and state/local government managers and CEOs

Industry/Entity Type

Health

Contact Information for Business Card

Fiona Tremblay
Executive Officer
Stronger Living Compact for the Plains
Ph: 0438 592 614
Fiona.Tremblay@qn.org.au

Requirements
Must have
• logo and details as provided.
Would prefer matt finish
I can't see that logo has successfully attached so if it has not, please email or call me to follow up.

```html
<!DOCTYPE html>
<html lang="en">
<head>
<meta charset="utf-8">
<title>Business Card – Fiona Tremblay</title>
<link href="https://fonts.googleapis.com/css2?family=Lato:wght@300;400;700&display=swap" rel="stylesheet">
<style>
  :root {
    --blue: #1b8fd2;
    --blue-deep: #0d75bd;
    --blue-light: #3aa6e0;
    --white: #ffffff;
    --ink-blue: #1377bf;
    --backdrop: #2a2a2c;
  }
  * { margin: 0; padding: 0; box-sizing: border-box; }
  html, body {
    width: 1200px; height: 800px; overflow: hidden;
    background: var(--backdrop);
    font-family: "Lato", Arial, sans-serif;
  }
  .sheet {
    width: 1200px; height: 800px;
    display: flex; align-items: center; justify-content: center; gap: 40px;
  }
  .card {
    position: relative; width: 540px; height: 330px; overflow: hidden;
    box-shadow: 0 10px 30px rgba(0,0,0,.45);
  }

  /* Front */
  .card--front {
    background: linear-gradient(160deg, var(--blue-light), var(--blue) 55%, var(--blue-deep));
  }
  .card--front .deco { position: absolute; inset: 0; }
  .name-band {
    position: absolute; left: 0; right: 0; top: 78px; height: 108px;
    background: var(--white);
  }
  .brand-mark {
    position: absolute; top: 40px; left: 50%; transform: translateX(-50%);
    display: flex; align-items: center; gap: 6px;
    color: var(--white); font-weight: 700; font-size: 13px; letter-spacing: 1px;
  }
  .brand-mark__dot {
    width: 12px; height: 12px; border-radius: 50%; background: var(--white);
  }
  .role {
    position: absolute; right: 34px; top: 94px; text-align: right;
    color: var(--ink-blue); font-weight: 700; font-size: 10.5px; line-height: 1.25;
    text-transform: uppercase; letter-spacing: .3px;
  }
  .holder-name {
    position: absolute; left: 0; right: 0; top: 124px; text-align: center;
    color: var(--ink-blue); font-weight: 700; font-size: 42px; letter-spacing: .5px;
    text-transform: uppercase;
  }
  .contact {
    position: absolute; left: 0; right: 0; top: 222px; text-align: center;
    color: var(--white); font-weight: 300; font-size: 13px; line-height: 1.45;
    text-transform: uppercase; letter-spacing: .3px;
  }
  .contact__rule {
    width: 90px; height: 1px; background: rgba(255,255,255,.8); margin: 6px auto;
  }

  /* Back */
  .card--back { background: var(--white); }
  .card--back .deco { position: absolute; inset: 0; }
  .back-brand {
    position: absolute; left: 0; right: 0; top: 140px;
    display: flex; align-items: center; justify-content: center; gap: 10px;
    color: var(--ink-blue); font-weight: 700; font-size: 17px;
    text-transform: uppercase; letter-spacing: .4px;
  }
  .back-brand__dot {
    width: 20px; height: 20px; border-radius: 50%; background: var(--ink-blue);
  }
</style>
</head>
<body>
<main class="sheet">
  <section class="card card--front" aria-label="Business card front">
    <svg class="deco" width="540" height="330" viewBox="0 0 540 330" aria-hidden="true">
      <circle cx="120" cy="250" r="150" fill="rgba(255,255,255,.07)"/>
      <circle cx="460" cy="60" r="110" fill="rgba(255,255,255,.06)"/>
    </svg>
    <div class="brand-mark"><span class="brand-mark__dot"></span>SLCP</div>
    <div class="name-band"></div>
    <p class="role">Executive Officer<br>Stronger Living Compact for the Plains</p>
    <h1 class="holder-name">Fiona Tremblay</h1>
    <div class="contact">
      <div class="contact__rule"></div>
      <p>Ph: 0438 592 614</p>
      <p>Fiona.Tremblay@qn.org.au</p>
      <div class="contact__rule"></div>
    </div>
  </section>

  <section class="card card--back" aria-label="Business card back">
    <svg class="deco" width="540" height="330" viewBox="0 0 540 330" aria-hidden="true">
      <path d="M380 0 H540 V330 H470 C560 230 520 80 380 0 Z" fill="var(--blue)"/>
      <path d="M0 330 V250 C40 290 90 315 150 330 Z" fill="var(--blue)"/>
      <circle cx="130" cy="250" r="120" fill="rgba(27,143,210,.06)"/>
    </svg>
    <div class="back-brand"><span class="back-brand__dot"></span>Stronger Living Compact for the Plains</div>
  </section>
</main>
</body>
</html>
```